"Principles for action" poster design for inside company

I would like to create a poster in order to make a message from CEO to employees to be clearly.
A size is A3E(landscape) , and I wish you to design 3 messages(principles for action) into one poster.
("Principles for action" is core value for employees to do everything on working in our company.)
I want you to design and place 3 messages as if they have some relations each other in one poster.
Principles for actions are as follows;
(1)Bird's eye view:
(Meaning: Although there are multiple right answers, it is difficult to gain something if you do not have different view from common one. We request you always to compare subjective view and objective view and then aim to have the specific view.)
(2)Agility:
(Meaning: Maximum rapidity is obtained in any case. Rapid accumulation of trivial reply, delivery, and courtesy, and it will lead to overall competitiveness.)
(3)Back to comfort:
(Meaning:Whatever the type of business be, various ideas are generated by employees. Those born in uncomfortable environment, become bad product that are not comfortable. In other words, managers will be asked to keep the comfortable environment.)
(Summary)
Our company always require employees that "First, you grasp the meaning of everything as if having bird's eyes, and do action rapidly. if you do action rapidly, a lot of important things will be appeared, so that you grasp again on bird's eye.
In order to be these situation worked, it must be always required comfortable environment for employees, so that manager have to create and maintain comfortable environment.
-
No need to add the "meanings" of 3 message, but please place 3 message(Bird's eye view, Agility and Back to comfort) into a poster.
We like some desings below, but you don't need to be swayed too much by them. That is to say, we dont like messy design.
http://www.pixelvantor.net/design/58203
http://www.pixelvantor.net/design/47261
http://www.pixelvantor.net/design/39482
http://www.pixelvantor.net/design/2837465/poster-design-by-plume
http://www.pixelvantor.net/design/2837467/poster-design-by-plume
http://www.pixelvantor.net/design/2649031/poster-design-by-mossylantern
-
the attachment file is the logo data of our company. Please place it anywhere in the poster.

```html
<!DOCTYPE html>
<html lang="en">
<head>
<meta charset="utf-8">
<title>Principles for Action</title>
<link rel="stylesheet" href="https://fonts.googleapis.com/css2?family=Bodoni+Moda:opsz,wght@6..96,400;6..96,500;6..96,600&display=swap">
<style>
  :root {
    --paper: #ffffff;
    --frame: #b9b9b9;
    --road-edge: #a8a8a8;
    --road-type-light: #cfcfcf;
    --road-type-mid: #b3b3b3;
    --sign-blue: #0b93dc;
    --sign-edge: #1f1f6e;
    --post-navy: #2a1a6b;
    --ink-black: #0c0c0c;
    --ink-white: #ffffff;
    --brand-blue: #2a8fc1;
    --badge-shadow: #9a9a9a;
  }
  html, body {
    margin: 0;
    padding: 0;
    width: 1200px;
    height: 848px;
    overflow: hidden;
    background: var(--paper);
  }
  .poster {
    display: block;
    width: 1200px;
    height: 848px;
  }
  .poster-frame { fill: var(--paper); stroke: var(--frame); stroke-width: 1.5; }
  .road-edge { fill: none; stroke: var(--road-edge); stroke-width: 1; }
  .road-type {
    font-family: "Bodoni Moda", "Didot", serif;
    font-weight: 500;
  }
  .road-type--light { fill: var(--road-type-light); }
  .road-type--mid { fill: var(--road-type-mid); }
  .sign-post { fill: var(--post-navy); }
  .sign-panel { fill: var(--sign-blue); stroke: var(--sign-edge); stroke-width: 1.2; }
  .sign-text {
    font-family: "Bodoni Moda", "Didot", serif;
    font-weight: 500;
    text-anchor: middle;
  }
  .sign-text--black { fill: var(--ink-black); }
  .sign-text--white { fill: var(--ink-white); }
  .brand-shadow { fill: var(--badge-shadow); }
  .brand-box { fill: var(--paper); stroke: var(--ink-black); stroke-width: 1.2; }
  .brand-name {
    font-family: "Bodoni Moda", "Didot", serif;
    font-weight: 500;
    fill: var(--brand-blue);
  }
</style>
</head>
<body>
<svg class="poster" viewBox="0 0 1037 733" preserveAspectRatio="none" role="img" aria-label="Principles for Action: Bird's Eye View, Agility, Back to Comfort">
  <rect class="poster-frame" x="0.75" y="0.75" width="1035.5" height="731.5"/>

  <path class="road-edge" d="M0,195 C260,225 520,320 1037,705"/>
  <path class="road-edge" d="M0,442 C330,505 620,585 830,733"/>

  <g class="road-type road-type--light">
    <text transform="translate(52,448) rotate(-55)" font-size="30" textLength="215" lengthAdjust="spacingAndGlyphs">PRINCIPLES</text>
    <text transform="translate(150,478) rotate(-55)" font-size="92" textLength="180" lengthAdjust="spacingAndGlyphs">FOR</text>
    <text transform="translate(285,548) rotate(-55)" font-size="56" textLength="215" lengthAdjust="spacingAndGlyphs">ACTION</text>
  </g>

  <g class="road-type road-type--mid">
    <text transform="translate(420,612) rotate(-55)" font-size="28" textLength="205" lengthAdjust="spacingAndGlyphs">PRINCIPLES</text>
    <text transform="translate(512,645) rotate(-55)" font-size="86" textLength="175" lengthAdjust="spacingAndGlyphs">FOR</text>
    <text transform="translate(640,712) rotate(-55)" font-size="54" textLength="205" lengthAdjust="spacingAndGlyphs">ACTION</text>
  </g>

  <g class="sign sign--view">
    <rect class="sign-post" x="157" y="5" width="20" height="243"/>
    <polygon class="sign-panel" points="55,13 268,60 268,172 55,128"/>
    <g transform="translate(161.5,0) skewY(12.4)">
      <text class="sign-text sign-text--black" x="0" y="82" font-size="26" textLength="200" lengthAdjust="spacingAndGlyphs">BIRD’S EYE</text>
      <text class="sign-text sign-text--white" x="-6" y="140" font-size="50" textLength="118" lengthAdjust="spacingAndGlyphs">VIEW</text>
    </g>
  </g>

  <g class="sign sign--agility">
    <rect class="sign-post" x="437" y="35" width="26" height="325"/>
    <polygon class="sign-panel" points="303,48 586,110 586,262 303,200"/>
    <g transform="translate(444.5,0) skewY(12.4)">
      <text class="sign-text sign-text--white" x="0" y="190" font-size="98" textLength="255" lengthAdjust="spacingAndGlyphs">AGILITY</text>
    </g>
  </g>

  <g class="sign sign--comfort">
    <rect class="sign-post" x="810" y="128" width="38" height="452"/>
    <polygon class="sign-panel" points="626,148 1015,235 1015,440 626,355"/>
    <g transform="translate(820.5,0) skewY(12.6)">
      <text class="sign-text sign-text--black" x="12" y="268" font-size="80" textLength="275" lengthAdjust="spacingAndGlyphs">BACK TO</text>
      <text class="sign-text sign-text--white" x="2" y="366" font-size="108" textLength="345" lengthAdjust="spacingAndGlyphs">COMFORT</text>
    </g>
  </g>

  <g class="brand">
    <rect class="brand-shadow" x="13" y="617" width="402" height="110"/>
    <rect class="brand-box" x="8" y="612" width="402" height="110"/>
    <text class="brand-name" x="209" y="688" font-size="58" text-anchor="middle">tandemly</text>
  </g>
</svg>
</body>
</html>
```